Calderwyn Structural Roof Inc.

We need a business card design for a commercial roofing company metro Boston based. We are a roofing company that help people manage buildings and build relationships with clients. We would like a unique card that stands out. We want a business card with a white background. We do not want a roof as the logo.

Industry/Entity Type

Roofing

```html
<!DOCTYPE html>
<html lang="en">
<head>
<meta charset="utf-8">
<title>Calderwyn Structural Roof Inc. — Business Card</title>
<link href="https://fonts.googleapis.com/css2?family=Oswald:wght@300;400&family=Arimo:wght@400&display=swap" rel="stylesheet">
<style>
  :root {
    --backdrop: #e4e1dc;
    --card-white: #ffffff;
    --card-tint: #f6f6f9;
    --navy: #141638;
    --gold: #eaa918;
    --head-font: "Oswald", sans-serif;
    --body-font: "Arimo", sans-serif;
  }
  html, body {
    margin: 0;
    padding: 0;
    width: 1200px;
    height: 1000px;
    overflow: hidden;
    background: var(--backdrop);
  }
  .canvas {
    position: relative;
    width: 1200px;
    height: 1000px;
  }
  .card {
    position: absolute;
    left: 210px;
    width: 780px;
    height: 446px;
    background: radial-gradient(ellipse at 55% 45%, var(--card-white) 0%, var(--card-tint) 80%);
    box-shadow: 0 8px 22px rgba(0,0,0,0.18);
    overflow: hidden;
    color: var(--navy);
  }
  .card-front { top: 42px; }
  .card-back { top: 512px; }

  /* Front */
  .brand-block {
    position: absolute;
    top: 120px;
    left: 0;
    right: 0;
    text-align: center;
  }
  .brand-mark {
    display: inline-block;
    width: 54px;
    height: 54px;
    background: var(--gold);
    margin-bottom: 18px;
  }
  .brand-name {
    font-family: var(--head-font);
    font-weight: 300;
    font-size: 34px;
    letter-spacing: 1px;
    color: var(--gold);
    text-transform: uppercase;
    line-height: 1;
  }
  .brand-sub {
    display: flex;
    align-items: center;
    justify-content: center;
    gap: 22px;
    margin-top: 12px;
  }
  .brand-sub .rule {
    width: 46px;
    height: 2px;
    background: var(--gold);
  }
  .brand-sub .word {
    font-family: var(--body-font);
    font-size: 18px;
    letter-spacing: 22px;
    margin-right: -22px;
    color: var(--navy);
  }
  .web-band {
    position: absolute;
    left: 0;
    right: 0;
    bottom: 40px;
    display: flex;
    align-items: center;
    gap: 12px;
  }
  .web-band .bar {
    flex: 1;
    height: 6px;
    background: var(--gold);
  }
  .web-band .url {
    font-family: var(--body-font);
    font-size: 14px;
    color: var(--navy);
  }

  /* Back */
  .side-accent {
    position: absolute;
    left: 0;
    top: 60px;
    width: 8px;
    height: 130px;
    background: var(--gold);
  }
  .company {
    position: absolute;
    left: 44px;
    top: 70px;
    display: flex;
    align-items: flex-start;
    gap: 22px;
  }
  .company-mark {
    width: 70px;
    height: 70px;
    background: var(--gold);
    margin-top: 16px;
  }
  .company-name {
    font-family: var(--head-font);
    font-weight: 300;
    font-size: 26px;
    color: var(--gold);
    text-transform: uppercase;
    letter-spacing: 0.5px;
    line-height: 1.1;
  }
  .company-address {
    font-family: var(--body-font);
    font-size: 19px;
    line-height: 1.35;
    margin-top: 6px;
  }
  .contacts {
    position: absolute;
    top: 170px;
    right: 30px;
    display: flex;
    gap: 28px;
    align-items: flex-start;
  }
  .person {
    font-family: var(--body-font);
    font-size: 19px;
    line-height: 1.35;
  }
  .person-primary {
    text-align: right;
    margin-top: 70px;
  }
  .person-name {
    font-family: var(--body-font);
    font-size: 27px;
    color: var(--gold);
    line-height: 1.2;
  }
  .person-secondary .person-name { margin-bottom: 8px; }
  .line-with-icon {
    display: flex;
    align-items: center;
    gap: 10px;
  }
  .icon {
    width: 20px;
    height: 20px;
    flex: none;
  }
</style>
</head>
<body>
<main class="canvas">

  <section class="card card-front" aria-label="Card front">
    <div class="brand-block">
      <span class="brand-mark" aria-hidden="true"></span>
      <div class="brand-name">Calderwyn Structural</div>
      <div class="brand-sub">
        <span class="rule"></span>
        <span class="word">ROOF</span>
        <span class="rule"></span>
      </div>
    </div>
    <div class="web-band">
      <span class="bar"></span>
      <span class="url">www.calderwynroof.com</span>
      <span class="bar"></span>
    </div>
  </section>

  <section class="card card-back" aria-label="Card back">
    <span class="side-accent" aria-hidden="true"></span>
    <div class="company">
      <span class="company-mark" aria-hidden="true"></span>
      <div>
        <div class="company-name">Calderwyn Structural Roof Inc.</div>
        <div class="company-address">214 Alder Wharf Rd<br>Brackton , Ma. 02190-3318</div>
      </div>
    </div>

    <div class="contacts">
      <div class="person person-primary">
        <div class="person-name">Mateo Varga</div>
        <div>President</div>
        <div>mateo@calderwynroof.com</div>
        <div>Direct 781-555-0148</div>
      </div>
      <div class="person person-secondary">
        <div class="person-name">Owen Callister</div>
        <div class="line-with-icon">
          <svg class="icon icon-mail" viewBox="0 0 20 20" aria-hidden="true">
            <circle cx="10" cy="10" r="10" fill="#eaa918"/>
            <rect x="5" y="6.5" width="10" height="7" fill="none" stroke="#ffffff" stroke-width="1.3"/>
            <polyline points="5,6.5 10,10.5 15,6.5" fill="none" stroke="#ffffff" stroke-width="1.3"/>
          </svg>
          <span>owen@calderwynroof.com</span>
        </div>
        <div class="line-with-icon">
          <svg class="icon icon-phone" viewBox="0 0 20 20" aria-hidden="true">
            <circle cx="10" cy="10" r="10" fill="#eaa918"/>
            <rect x="7" y="4.5" width="6" height="11" rx="1" fill="none" stroke="#ffffff" stroke-width="1.4"/>
            <line x1="9" y1="13.5" x2="11" y2="13.5" stroke="#ffffff" stroke-width="1.2"/>
          </svg>
          <span>Direct 781-555-0162</span>
        </div>
      </div>
    </div>
  </section>

</main>
</body>
</html>
```